Brisk Therapy Flyer - Physiotherapy company

I am looking for a two-sided flyer (4"x8") that can be easily posted on cork boards or displayed as needed to provide information about my business. I would like to use the colors found in my logo (see attached) along with white and black. Please have a look at my website for ideas of how I would like the color schemes etc (www.briskcare-demo.ca). I would like it to follow the same style as my website.<br/><br/>FRONT SIDE<br/>I am hoping to have the name of our business "Brisk Therapy" with our slogan "Boreal Physiotherapy - Rehab and Recovery Above the Pines (degrees symbol)" underneath. Somewhere above or around this I would like my logo (see attached). <br/><br/>Below that I would like a title "Services Provided" and then listed: <br/>Mobile Services<br/>Clinic<br/>Telehealth<br/><br/>Below that, I would like another title "Treatments Offered" and then listed: <br/>Hands-on manual therapy<br/>Intramuscular Stimulation (IMS)<br/>Acupuncture<br/>Athletic taping<br/>Injury/condition education<br/>Supervised exercise<br/><br/>Below that I would like "Contact Us":<br/>Brisk Therapy<br/>www.BriskCare-demo.ca<br/>Book online through https://briskcare.bookfake-demo.com/<br/>physio@briskcare-demo.ca<br/>867-555-0148<br/>Direct Billing offered for most extended health providers<br/>(Chatterly, Snapwell logo, kinelogix logo (see attached) on bottom maybe in corner or centered)<br/><br/>BACK SIDE<br/><br/>I would like the logo on there once again maybe. Then I would like these three information sections one on top of the other spaced out appropriately.<br/><br/>Image (needling image) (see attached)<br/>Title: Mobile Physiotherapy<br/>The information below title: If you want to keep moving and need some help, but your current condition makes it difficult or unsafe to travel to and from a clinic to see a physiotherapist, that’s where we come in. We make it easy by offering a mobile service that provides exceptional one-on-one physiotherapy assessment and treatment in the comfort of your own home. There is a small fee to access mobile services. <br/><br/>Image (Hands on knee image) (see attached)<br/>Title: Clinic<br/>The information below title: If you have an injury that is causing you pain or restricting you from doing the activities that you want to do then physiotherapy can help. A traditional approach to physiotherapy where you come to our clinic and we provide one to one education and hands on therapy. <br/><br/>Image (computer, tablet etc) (see attached)<br/>Title: Telehealth<br/>The information below title: If you live outside of Ridgeford or just want easy access to a physiotherapist from the comfort of your home, then Telehealth is for you. Telehealth involves meeting with your physiotherapist using real-time technology, similar to VidLink. Brisk Therapy utilizes Kinelogix for exercise prescription, pain tracking and telehealth. Through Kinelogix or it’s Motivapp you can discuss your treatment plan, diagnoses, exercises, daily activities or any other questions you may have directly with a physiotherapist.<br/><br/><br/><br/>

Industry/Entity Type

Healthcare

Colors

Designer to choose colors to be used in the design.

Requirements
Must have
• Follow the same colors and schemes of my website (www.briskcare-demo.ca)
• Keep it clean and concise
Nice to have
• Images might not fit because I don't want it too cluttered.
Should not have
• Too busy

```html
<!DOCTYPE html>
<html lang="en">
<head>
<meta charset="utf-8">
<title>Brisk Therapy Flyer</title>
<link href="https://fonts.googleapis.com/css2?family=Libre+Baskerville:wght@400;700&family=Montserrat:wght@500;600;700&family=Source+Sans+3:wght@400;600&display=swap" rel="stylesheet">
<style>
  :root{
    --navy:#27446e;
    --navy-deep:#2b4a75;
    --green:#1d5a48;
    --green-line:#2c6e5c;
    --teal:#45b89c;
    --ink:#1f1f1f;
    --white:#ffffff;
    --page:#616161;
    --sky-top:#ffffff;
    --sky-low:#dfe7f3;
  }
  *{box-sizing:border-box;margin:0;padding:0}
  html,body{width:1200px;height:1200px;overflow:hidden;background:var(--page)}
  body{position:relative;font-family:"Source Sans 3",Arial,sans-serif;color:var(--ink)}

  .flyer{position:absolute;top:189px;width:417px;height:833px;background:var(--white);overflow:hidden}
  .flyer--front{left:110px;background:linear-gradient(180deg,var(--sky-top) 0%,var(--sky-low) 30%,var(--white) 58%)}
  .flyer--back{left:608px}

  /* front header */
  .brand-title{position:absolute;top:30px;left:0;width:100%;text-align:center;font-family:"Libre Baskerville",Georgia,serif;font-weight:700;font-size:32px;color:var(--navy);letter-spacing:.5px}
  .brand-region{position:absolute;top:92px;left:0;width:100%;text-align:center;font-family:"Libre Baskerville",Georgia,serif;font-weight:700;font-size:17.5px;color:var(--green)}
  .brand-slogan{position:absolute;top:120px;left:0;width:100%;text-align:center;font-family:"Libre Baskerville",Georgia,serif;font-size:17px;color:var(--navy)}

  .hero-photo{position:absolute;top:178px;left:0;width:417px;height:320px;
    background:linear-gradient(180deg,rgba(223,231,243,0) 0%,#b7c6e0 18%,#8ea3c8 42%,#6d7a98 62%,#6b5447 82%,#4a3a31 100%)}
  .hero-cut{position:absolute;top:370px;left:0;width:417px;height:130px}

  .logo-name{position:absolute;top:466px;left:0;width:100%;text-align:center;font-family:"Libre Baskerville",Georgia,serif;font-weight:700;font-size:21px;color:var(--green);letter-spacing:2px}

  /* services */
  .services{position:absolute;top:540px;left:25px;width:367px;height:89px;border:1.5px solid var(--green);border-radius:7px}
  .pill-label{position:absolute;top:-11px;left:50%;transform:translateX(-50%);width:186px;height:20px;background:var(--green);color:var(--white);font-family:"Montserrat",Arial,sans-serif;font-weight:700;font-size:12px;letter-spacing:.6px;text-align:center;line-height:20px;border-radius:3px}
  .service{position:absolute;top:14px;width:110px;text-align:center}
  .service svg{display:block;margin:0 auto}
  .service-name{display:block;margin-top:4px;font-family:"Montserrat",Arial,sans-serif;font-weight:500;font-size:12.5px;color:var(--ink)}
  .service--mobile{left:10px}
  .service--clinic{left:128px}
  .service--tele{left:252px}

  /* treatments */
  .treatments-title{position:absolute;top:648px;left:0;width:100%;text-align:center;font-family:"Montserrat",Arial,sans-serif;font-weight:700;font-size:13.5px;color:var(--navy);letter-spacing:.4px}
  .treatments{position:absolute;top:669px;list-style:none;font-size:13.2px;line-height:20.5px;color:var(--ink)}
  .treatments--left{left:32px}
  .treatments--right{left:259px}
  .treatments li{position:relative;padding-left:12px}
  .treatments li::before{content:"";position:absolute;left:0;top:7px;width:7px;height:7px;border-radius:50%;background:var(--green)}

  /* footers */
  .footer{position:absolute;left:0;bottom:0;width:100%;background:var(--navy-deep);border-top:2px solid var(--green-line);color:var(--white)}
  .flyer--front .footer{height:80px}
  .flyer--back .footer{height:95px}
  .book-pill{position:absolute;top:740px;left:57px;width:304px;height:21px;background:var(--green);border:1px solid #4f8d7b;border-radius:11px;color:var(--white);font-size:11px;text-align:center;line-height:19px;z-index:2}
  .contact-row{position:absolute;top:24px;left:26px;width:366px;display:flex;justify-content:space-between;font-size:11px}
  .contact-item{display:flex;align-items:center;gap:4px;white-space:nowrap}
  .billing{position:absolute;top:46px;left:31px;font-size:10px;letter-spacing:-.2px}
  .app-name{font-family:"Source Sans 3",Arial,sans-serif;font-weight:600;color:var(--teal)}
  .flyer--front .app-name{position:absolute;top:43px;left:275px;font-size:14px}
  .social{font-size:8.5px;color:var(--white)}
  .flyer--front .social{position:absolute;top:49px;left:340px;display:flex;gap:6px}

  /* back */
  .feature-photo{position:absolute;left:26px;width:365px;height:105px;border:1px solid #9aa9c2}
  .feature-photo--needling{top:26px;background:linear-gradient(90deg,#f2f2f3 0%,#e9d3c6 45%,#e2b8a0 75%,#d9a487 100%)}
  .feature-photo--clinic{top:269px;background:linear-gradient(90deg,#8d8d8d 0%,#c49b83 35%,#3a3b40 60%,#eaeaea 100%)}
  .feature-photo--tele{top:481px;background:linear-gradient(90deg,#d0d0d0 0%,#cfcfcf 25%,#f4f4f4 50%,#cfcfcf 75%,#d0d0d0 100%)}
  .feature-title{position:absolute;left:0;width:100%;text-align:center;font-family:"Montserrat",Arial,sans-serif;font-weight:700;font-size:12.5px;color:var(--navy);letter-spacing:.4px}
  .feature-text{position:absolute;left:26px;width:365px;font-size:11.2px;line-height:14.8px;text-align:justify;color:var(--ink)}
  .back-name{position:absolute;top:36px;left:20px;width:82px;text-align:center;font-family:"Libre Baskerville",Georgia,serif;font-weight:700;font-size:13px;line-height:16px;color:var(--white);letter-spacing:1px}
  .back-contact{position:absolute;top:18px;left:120px;font-size:12px;line-height:17.5px}
  .back-contact .contact-item{gap:6px}
  .flyer--back .social{position:absolute;top:22px;left:330px;display:flex;gap:8px}
  .flyer--back .app-name{position:absolute;top:48px;left:306px;font-size:17px}
</style>
</head>
<body>

<section class="flyer flyer--front">
  <h1 class="brand-title">BRISK THERAPY</h1>
  <p class="brand-region">BOREAL PHYSIOTHERAPY</p>
  <p class="brand-slogan">Rehab and Recovery Above the Pines°</p>

  <div class="hero-photo" role="img" aria-label="Photo of two hikers climbing a rocky ridge with misty blue mountains behind"></div>
  <svg class="hero-cut" viewBox="0 0 417 130" aria-hidden="true">
    <polygon points="0,121 207,3 417,115 417,130 0,130" fill="#ffffff"/>
    <polyline points="0,121 207,3 417,115" fill="none" stroke="#1d5a48" stroke-width="5"/>
  </svg>
  <p class="logo-name">BRISK THERAPY</p>

  <div class="services">
    <span class="pill-label">SERVICES PROVIDED</span>
    <div class="service service--mobile">
      <svg width="44" height="44" viewBox="0 0 44 44" aria-hidden="true">
        <circle cx="22" cy="22" r="21" fill="#1d5a48"/><circle cx="22" cy="22" r="18" fill="#27446e"/>
        <path d="M11 26 V20 H20 L24 16 H31 V26 Z" fill="none" stroke="#fff" stroke-width="1.4"/>
        <circle cx="15.5" cy="27" r="2.3" fill="#27446e" stroke="#fff" stroke-width="1.3"/>
        <circle cx="27.5" cy="27" r="2.3" fill="#27446e" stroke="#fff" stroke-width="1.3"/>
      </svg>
      <span class="service-name">Mobile Services</span>
    </div>
    <div class="service service--clinic">
      <svg width="44" height="44" viewBox="0 0 44 44" aria-hidden="true">
        <circle cx="22" cy="22" r="21" fill="#1d5a48"/><circle cx="22" cy="22" r="18" fill="#27446e"/>
        <rect x="14" y="11" width="16" height="20" fill="none" stroke="#fff" stroke-width="1.4"/>
        <g fill="#fff"><rect x="17" y="14" width="3" height="3"/><rect x="24" y="14" width="3" height="3"/><rect x="17" y="19" width="3" height="3"/><rect x="24" y="19" width="3" height="3"/><rect x="20" y="25" width="4" height="6"/></g>
      </svg>
      <span class="service-name">Clinic</span>
    </div>
    <div class="service service--tele">
      <svg width="44" height="44" viewBox="0 0 44 44" aria-hidden="true">
        <circle cx="22" cy="22" r="21" fill="#1d5a48"/><circle cx="22" cy="22" r="18" fill="#27446e"/>
        <rect x="11" y="12" width="22" height="15" rx="1.5" fill="none" stroke="#fff" stroke-width="1.4"/>
        <path d="M18 31 H26 M22 27 V31" stroke="#fff" stroke-width="1.4"/>
        <path d="M13 20 H17 L19 16 L22 24 L24 19 H31" fill="none" stroke="#fff" stroke-width="1.2"/>
      </svg>
      <span class="service-name">Telehealth</span>
    </div>
  </div>

  <h2 class="treatments-title">TREATMENTS OFFERED</h2>
  <ul class="treatments treatments--left">
    <li>Hands-on manual therapy</li>
    <li>Intramuscular Stimulation(IMS)</li>
    <li>Injury/condition education</li>
  </ul>
  <ul class="treatments treatments--right">
    <li>Acupuncture</li>
    <li>Athletic taping</li>
    <li>Supervised exercise</li>
  </ul>

  <p class="book-pill">Book online through https://briskcare.bookfake-demo.com/</p>
  <footer class="footer">
    <div class="contact-row">
      <span class="contact-item">
        <svg width="9" height="9" viewBox="0 0 10 10" aria-hidden="true"><path d="M2 1 L4 1 L4.6 3.2 L3.4 4.2 Q4.6 6 6 6.6 L7 5.4 L9 6 L9 8 Q5 9 1.5 4.5 Q1 3 2 1 Z" fill="#6cc3e0"/></svg>867-555-0148</span>
      <span class="contact-item">
        <svg width="10" height="8" viewBox="0 0 10 8" aria-hidden="true"><rect x="0.5" y="0.5" width="9" height="7" fill="none" stroke="#6cc3e0"/><path d="M0.5 0.5 L5 4.5 L9.5 0.5" fill="none" stroke="#6cc3e0"/></svg>physio@briskcare-demo.ca</span>
      <span class="contact-item">
        <svg width="9" height="9" viewBox="0 0 10 10" aria-hidden="true"><circle cx="5" cy="5" r="4.3" fill="none" stroke="#6cc3e0"/><path d="M0.7 5 H9.3 M5 0.7 Q2.5 5 5 9.3 M5 0.7 Q7.5 5 5 9.3" fill="none" stroke="#6cc3e0" stroke-width=".8"/></svg>www.BriskCare-demo.ca</span>
    </div>
    <p class="billing">Direct Billing offered for most extended health providers</p>
    <span class="app-name">Motivapp</span>
    <div class="social"><span>Chatterly</span><span>Snapwell</span></div>
  </footer>
</section>

<section class="flyer flyer--back">
  <div class="feature-photo feature-photo--needling" role="img" aria-label="Close-up photo of hands placing acupuncture needles in a shoulder"></div>
  <h2 class="feature-title" style="top:141px">MOBILE PHYSIOTHERAPY</h2>
  <p class="feature-text" style="top:157px">If you want to keep moving and need some help, but your current condition makes it difficult or unsafe to travel to and from a clinic to see a physiotherapist, that’s where we come in. We make it easy by offering a mobile service that provides exceptional one-on-one physiotherapy assessment and treatment in the comfort of your own home. There is a small fee to access mobile services.</p>

  <div class="feature-photo feature-photo--clinic" role="img" aria-label="Photo of a therapist's hands treating a patient's knee on a treatment table"></div>
  <h2 class="feature-title" style="top:382px">CLINIC</h2>
  <p class="feature-text" style="top:398px">If you have an injury that is causing you pain or restricting you from doing the activities that you want to do then physiotherapy can help. A traditional approach to physiotherapy where you come to our clinic and we provide one to one education and hands on therapy.</p>

  <div class="feature-photo feature-photo--tele" role="img" aria-label="Image of a laptop, tablet and phone showing an exercise and video-call app"></div>
  <h2 class="feature-title" style="top:593px">TELEHEALTH</h2>
  <p class="feature-text" style="top:609px">If you live outside of Ridgeford or just want easy access to a physiotherapist from the comfort of your home, then Telehealth is for you. Telehealth involves meeting with your physiotherapist using real-time technology, similar to VidLink. Brisk Therapy utilizes Kinelogix for exercise prescription, pain tracking and telehealth. Through Kinelogix or it’s Motivapp you can discuss your treatment plan, diagnoses, exercises, daily activities or any other questions you may have directly with a physiotherapist.</p>

  <footer class="footer">
    <p class="back-name">BRISK THERAPY</p>
    <div class="back-contact">
      <span class="contact-item">
        <svg width="10" height="10" viewBox="0 0 10 10" aria-hidden="true"><path d="M2 1 L4 1 L4.6 3.2 L3.4 4.2 Q4.6 6 6 6.6 L7 5.4 L9 6 L9 8 Q5 9 1.5 4.5 Q1 3 2 1 Z" fill="#6cc3e0"/></svg>867-555-0148</span>
      <span class="contact-item">
        <svg width="10" height="8" viewBox="0 0 10 8" aria-hidden="true"><rect x="0.5" y="0.5" width="9" height="7" fill="none" stroke="#6cc3e0"/><path d="M0.5 0.5 L5 4.5 L9.5 0.5" fill="none" stroke="#6cc3e0"/></svg>physio@briskcare-demo.ca</span>
      <span class="contact-item">
        <svg width="10" height="10" viewBox="0 0 10 10" aria-hidden="true"><circle cx="5" cy="5" r="4.3" fill="none" stroke="#6cc3e0"/><path d="M0.7 5 H9.3 M5 0.7 Q2.5 5 5 9.3 M5 0.7 Q7.5 5 5 9.3" fill="none" stroke="#6cc3e0" stroke-width=".8"/></svg>www.BriskCare-demo.ca</span>
    </div>
    <div class="social"><span>Chatterly</span><span>Snapwell</span></div>
    <span class="app-name">Motivapp</span>
  </footer>
</section>

</body>
</html>
```